TrailNorth Site Refresh - redesign to improve visitor journeys and conversions

I need my website brought to life, professional and engaging.
I can supply as much pictures as needed to create enhancing visuals. I need your team to review the website and create a list of ideas of what you need from me to bring this vision to life.
The company does 3d modeling, 3d printing with FDM and resin printers, CAD design, 3d scanning.
My website is https://qrfabworksco.example/
Please review it and give me your best.
Target Market(s)
cosplayer, filmmakers, life size prints, custom designs, redesign and scanning, large and small scale prints, replicating
Industry/Entity Type
CAD Design, Additive Manufacturing, 3D Printing, 3D Scanning
Coding
Coded - Design and coding required
Number of Pages Required
3 page
Font styles to use
Requirements
Must have
- Professional and clean look, inviting, eye grabber

```html
<!DOCTYPE html>
<html lang="en">
<head>
<meta charset="utf-8">
<title>What I need from your side (to finalize)</title>
<link href="https://fonts.googleapis.com/css2?family=Tinos:wght@400;700&display=swap" rel="stylesheet">
<style>
  :root {
    --page-bg: #ffffff;
    --ink: #000000;
  }
  html, body {
    margin: 0;
    padding: 0;
    background: var(--page-bg);
    overflow: hidden;
  }
  .page {
    position: relative;
    width: 1200px;
    height: 850px;
    overflow: hidden;
    background: var(--page-bg);
    color: var(--ink);
    font-family: "Tinos", "Times New Roman", serif;
  }
  .page-title {
    position: absolute;
    left: 61px;
    top: 72px;
    margin: 0;
    font-size: 52px;
    line-height: 60px;
    font-weight: 700;
    letter-spacing: -0.2px;
  }
  .request-list {
    position: absolute;
    left: 147px;
    top: 197px;
    width: 1010px;
    margin: 0;
    padding: 0;
    list-style: none;
    font-size: 26.5px;
    line-height: 50.8px;
  }
  .request-item {
    position: relative;
  }
  .request-item::before {
    content: "";
    position: absolute;
    left: -43px;
    top: 22px;
    width: 6px;
    height: 6px;
    border-radius: 50%;
    background: var(--ink);
  }
  .request-item strong {
    font-weight: 700;
  }
</style>
</head>
<body>
  <main class="page">
    <h1 class="page-title">What I need from your side (to finalize)</h1>
    <ul class="request-list">
      <li class="request-item"><strong>Brand</strong>: logo (SVG/PNG), primary/secondary colors, preferred font(s).</li>
      <li class="request-item"><strong>Services</strong>: printer models, <strong>max build volumes</strong>, <strong>layer heights</strong>, <strong>tolerances</strong>, <strong>material</strong><br><strong>list</strong> (PLA, PETG, ABS/ASA, Nylon, CF-Nylon, resin types).</li>
      <li class="request-item"><strong>Capabilities</strong>: finishing options (sanding, painting, vapor smoothing, inserts), QC<br>steps, typical <strong>lead times</strong>.</li>
      <li class="request-item"><strong>Industries/use cases</strong>: (e.g., fixtures, enclosures, cosplay, robotics, dental models).</li>
      <li class="request-item"><strong>Top 10 portfolio images</strong> with one-line captions (process/material/finish).</li>
      <li class="request-item"><strong>Quote operations</strong>: where form submissions go (email/CRM), SLA for responses,<br>optional instant-quote rules.</li>
      <li class="request-item"><strong>Business info</strong>: address, phone, hours (confirm), veteran support blurb,<br>shipping/pickup policy, payment options.</li>
      <li class="request-item"><strong>Socials</strong> + 2–3 short testimonials.</li>
    </ul>
  </main>
</body>
</html>
```